Broschüre für Sprachschule für die Vorstellung der Leistungen
Zielgruppe
Es geht um eine Broschüre einer Sprachschule für die Vorstellung der Leistungen:
Sprachkurse: A1, A2, B1. B2, C1, Fachsprache Ärzte, Fachspräche Pflegepersonal, Fachsprache Ingenieure
Seminare: Businessplan für Migranten, Unternehmensführung für Migranten, Ausbildung zur Pflegefachkraft, Existenzgründung für Migranten
Aufgabenstellung
Es handelt sich um ein Sprachschule/Bildungszentrum. Farben: Royal Blau, Gold

```html
<!DOCTYPE html>
<html lang="de">
<head>
<meta charset="utf-8">
<title>Sprachkurse &amp; Seminare – Broschüre</title>
<link href="https://fonts.googleapis.com/css2?family=Open+Sans:wght@400;600;700&display=swap" rel="stylesheet">
<style>
  :root{
    --royal:#232b7e;
    --gold:#b7a264;
    --sand:#ddd0ad;
    --paper:#ffffff;
    --ground:#e4e4e4;
    --photo-warm:#b7a48c;
    --photo-cool:#8fa3b6;
  }
  *{box-sizing:border-box;margin:0;padding:0}
  html,body{width:1200px;height:1000px;overflow:hidden}
  body{background:var(--ground);font-family:"Open Sans",Arial,sans-serif;color:var(--royal);position:relative}
  .page,.spread{position:absolute;background:var(--paper);overflow:hidden;box-shadow:0 2px 6px rgba(0,0,0,.12)}
  .block{position:absolute}
  .photo{position:absolute;background:linear-gradient(135deg,var(--photo-warm),var(--photo-cool))}
  .blue{background:var(--royal)}
  .gold{background:var(--gold)}
  .sand{background:var(--sand)}

  .cover{left:135px;top:71px;width:294px;height:411px}
  .spread-a{left:464px;top:69px;width:568px;height:413px}
  .spread-b{left:137px;top:518px;width:571px;height:413px}
  .back{left:749px;top:518px;width:288px;height:413px}
  .fold{position:absolute;top:0;bottom:0;width:1px;background:rgba(0,0,0,.06)}

  .logo-box{position:absolute;background:var(--paper);display:flex;align-items:center;justify-content:center;font-weight:400;color:var(--royal);letter-spacing:.5px}
  .cover-title{position:absolute;color:#fff;font-size:19px;line-height:21px;font-weight:600;padding:14px 0 0 19px}
  .cover-intro{position:absolute;color:#fff;font-size:9.6px;line-height:12px}

  .section-title{position:absolute;color:var(--gold);font-size:19px;font-weight:600;letter-spacing:.5px}
  .level{position:absolute;color:#fff;font-weight:700;line-height:1}
  .schedule{position:absolute;color:#fff;font-size:6.5px;line-height:10.5px;text-align:right}
  .schedule strong{display:block;font-size:9px;font-weight:700;line-height:13px;letter-spacing:.3px}
  .schedule.left{text-align:left}

  .copy{position:absolute;font-size:6.5px;line-height:8.2px}
  .copy h3{font-size:9.5px;font-weight:400;line-height:11.5px;margin-bottom:8px;letter-spacing:.2px}
  .copy p{margin-bottom:8px}
  .copy ul{list-style:none;margin-bottom:8px}
  .copy li{padding-left:7px;position:relative;margin-bottom:5px}
  .copy li::before{content:"•";position:absolute;left:0}

  .contact{position:absolute;color:#f3ecd7;text-align:center;font-size:6.5px;line-height:8.5px;padding-top:10px}
  .contact strong{display:block;font-size:9.5px;font-weight:600;color:#fff;letter-spacing:.5px;margin-bottom:8px}
  .contact p{margin-bottom:7px}
</style>
</head>
<body>

<!-- Cover -->
<section class="page cover">
  <div class="photo" style="left:9px;top:8px;width:277px;height:270px" role="img" aria-label="Foto: drei Lernende arbeiten gemeinsam am Tisch mit Notizblöcken und Laptop"></div>
  <div class="logo-box" style="left:178px;top:8px;width:95px;height:42px;font-size:22px">LOGO</div>
  <div class="block blue" style="left:0;top:274px;width:294px;height:137px"></div>
  <h1 class="cover-title block gold" style="left:0;top:242px;width:222px;height:64px">SPRACHKURSE<br>&amp; SEMINARE</h1>
  <p class="cover-intro" style="left:20px;top:326px;width:262px">berum secto quibus cum se parum volupta temperum<br>fugia natus vero ma voluptatisi sequamusam rerchilli-<br>quo ea diaerum, iur</p>
</section>

<!-- Spread A1 / A2 -->
<section class="spread spread-a">
  <div class="fold" style="left:284px"></div>
  <div class="block sand" style="left:0;top:0;width:271px;height:165px"></div>
  <h2 class="section-title" style="left:30px;top:28px">SPRACHKURSE</h2>
  <div class="block blue" style="left:0;top:83px;width:94px;height:330px"></div>
  <div class="level" style="left:18px;top:118px;font-size:46px">A1</div>
  <div class="schedule" style="left:0;top:343px;width:80px"><strong>KURSZEITEN</strong>12 EINHEITEN<br>MO 19-20 UHR<br>DO 19-20 UHR</div>
  <div class="copy" style="left:123px;top:83px;width:140px">
    <h3>IMILIS MAIONE CUSAM<br>QUIBUS PELESTO</h3>
    <p>volorem consequ ibustia volenis et occum untusam, omniet verrum iliciliqui ut aut lame aut eos iliquunt estem. Officipsam il endi conseque experios sequi</p>
    <p>blaborit excepudae prae estrunt odicil ipis vollaut plabor sim repe num, volupta­tis dolo vit,</p>
    <ul>
      <li>suntis dem liquiat ecerrov itibus ad et et harcit autem con et doluptatasi te seribus,</li>
      <li>cor aliqui nossent estrum solore mo quia quam volor aut et elibus eiur,</li>
      <li>seque ilis erae occabor eicatem non preium volesti onsequi</li>
    </ul>
    <p>berum secto quibus cum se parum volupta temperum fugia natus vero ma voluptatisi sequamusam rerchilliquo ea diaerum, iur</p>
    <p>volorem consequ ibustia volenis et occum untusam, omniet verrum iliciliqui ut aut lame aut eos iliquunt estem. Officipsam il endi conseque experios sequi blaborit excepudae prae estrunt odicil ipis vollaut plabor sim repe num, voluptatis dolo vit,</p>
  </div>
  <div class="copy" style="left:322px;top:27px;width:145px">
    <h3>IMILIS MAIONE CUSAM<br>QUIBUS PELESTO</h3>
    <p>volorem consequ ibustia volenis et occum untusam, omniet verrum iliciliqui ut aut lame aut eos iliquunt estem. Officipsam il endi conseque experios sequi</p>
    <p>blaborit excepudae prae estrunt odicil ipis vollaut plabor sim repe num, volupta­tis dolo vit,</p>
    <ul>
      <li>suntis dem liquiat ecerrov itibus ad et et harcit autem con et doluptatasi te seribus,</li>
      <li>cor aliqui nossent estrum solore mo quia quam volor aut et elibus eiur,</li>
      <li>seque ilis erae occabor eicatem non preium volesti onsequi</li>
    </ul>
    <p>berum secto quibus cum se parum volupta temperum fugia natus vero ma voluptatisi sequamusam rerchilliquo ea diaerum, iur</p>
  </div>
  <div class="block blue" style="left:471px;top:0;width:97px;height:330px"></div>
  <div class="schedule left" style="left:486px;top:27px;width:80px"><strong>KURSZEITEN</strong>12 EINHEITEN<br>MO 19-20 UHR<br>DO 19-20 UHR</div>
  <div class="level" style="left:484px;top:282px;font-size:46px">A2</div>
  <div class="block gold" style="left:284px;top:330px;width:75px;height:83px"></div>
  <div class="block gold" style="left:540px;top:330px;width:28px;height:83px"></div>
  <div class="photo" style="left:359px;top:248px;width:112px;height:165px;background:linear-gradient(160deg,#e6e4df,#8a8d93)" role="img" aria-label="Foto: junger Mann mit Tablet und Kopfhörern"></div>
</section>

<!-- Spread B -->
<section class="spread spread-b">
  <div class="fold" style="left:285px"></div>
  <div class="block sand" style="left:68px;top:125px;width:217px;height:82px"></div>
  <div class="photo" style="left:31px;top:0;width:180px;height:167px;background:linear-gradient(160deg,#f2f1ee,#8fb0cf)" role="img" aria-label="Foto: junge Frau in Jeanshemd zeigt selbstbewusst ihre Stärke"></div>
  <div class="copy" style="left:125px;top:219px;width:140px">
    <h3>IMILIS MAIONE CUSAM<br>QUIBUS PELESTO</h3>
    <p>volorem consequ ibustia volenis et occum untusam, omniet verrum iliciliqui ut aut lame aut eos iliquunt estem. Officipsam il endi conseque experios sequi</p>
    <p>blaborit excepudae prae estrunt odicil ipis vollaut plabor sim repe num, volupta­tis dolo vit,</p>
    <ul>
      <li>suntis dem liquiat ecerrov itibus ad et et harcit autem con et doluptatasi te seribus,</li>
      <li>cor aliqui nossent estrum solore mo quia quam volor aut et elibus eiur,</li>
      <li>seque ilis erae occabor eicatem non preium volesti onsequi</li>
    </ul>
  </div>
  <div class="block blue" style="left:2px;top:248px;width:94px;height:165px"></div>
  <div class="schedule" style="left:2px;top:351px;width:80px"><strong>KURSZEITEN</strong>12 EINHEITEN<br>DI 19-20 UHR<br>MI 19-20 UHR</div>
  <div class="copy" style="left:313px;top:32px;width:230px">
    <h3>IMILIS MAIONE CUSAM QUIBUS PELESTO</h3>
    <p>volorem consequ ibustia volenis et occum untusam, omniet verrum iliciliqui ut aut lame aut eos iliquunt estem. Officipsam il endi conseque experios sequi blaborit excepudae prae estrunt odicil ipis vollaut plabor sim repe num, voluptatis dolo vit,</p>
    <p>suntis dem liquiat ecerrov itibus ad et et harcit autem con et dolupta­tasi te seribus, cor aliqui nossent estrum solore mo quia quam volor aut et elibus eiur, seque ilis erae occabor eicatem non preium volesti onsequi</p>
    <p>berum secto quibus cum se parum volupta temperum fugia natus vero ma voluptatisi sequamusam rerchilliquo ea diaerum, iur</p>
    <p>volorem consequ ibustia volenis et occum untusam, omniet verrum iliciliqui ut aut lame aut eos iliquunt estem. Officipsam il endi conseque experios sequi blaborit excepudae prae estrunt odicil ipis vollaut plabor sim repe num, voluptatis dolo vit.</p>
  </div>
  <div class="block gold" style="left:313px;top:286px;width:258px;height:87px"></div>
  <div class="photo" style="left:348px;top:248px;width:192px;height:165px;background:linear-gradient(135deg,#5b4a3c,#a7b4b0)" role="img" aria-label="Foto: zwei Lernende im Gespräch in einem hellen Raum"></div>
</section>

<!-- Back cover -->
<section class="page back">
  <div class="photo" style="left:9px;top:8px;width:270px;height:265px" role="img" aria-label="Foto: lachende Gruppe von Lernenden am Tisch mit Laptop"></div>
  <div class="block blue" style="left:0;top:275px;width:288px;height:138px"></div>
  <div class="logo-box" style="left:29px;top:275px;width:86px;height:42px;font-size:20px">LOGO</div>
  <div class="contact block gold" style="left:125px;top:332px;width:134px;height:79px">
    <strong>KONTAKT</strong>
    <p>Lindenweg 14<br>48151 Beispielstadt</p>
    <p>Tel. 0251 4830271<br>www.lernhaus-beispiel.de</p>
  </div>
</section>

</body>
</html>
```